Dr. Lumora needs a design for its website!

*Only need the design, coding is not required.
*Need desktop version ($500) and mobile/tablet version ($200)
*The attached files are not the exact layout we want, they are just for you to know what information should be included in those pages.
*The function of our website is like www.qavlo.hk
*For the background picture, prefer a lively picture and chinese people in it, NOT necessarily need a doctor or sick person in the picture

***Don't just copy the layout from the attachments or from the reference website, we are looking for creative ideas, non-ordinary designs!!!****

We are developing a website for the public to search a doctor by different criteria. At the initial stage, we need 4 pages to start with and other pages at later stage. I have attached the general idea of these pages but not necessarily to be exactly the same, I am looking for some new ideas.

This website needs a professional, modern, simple and user friendly design. The main color to be used in the website will be same as the color (R:0 G:139 B:205) used in our logo (see attached). We don't have any particular thoughts for the other color and the font to be used in the website. Can try to use circle outline for the icon in the navigation bar.

1. Home: will include 4 sections (see attached)

2. Doctor's details (see attached)

3. Health information: will include a short descriptions of this Health Info page and 5 sections (see attached)

4. News (see attached)

Reason: Not too many suitable designs to choose from and need more time to go through the designs

All

Medical

4 page

• must not be same as or looks too much like www.qavlo.hk
• prefer not to use black and red color

```html
<!DOCTYPE html>
<html lang="en">
<head>
<meta charset="utf-8">
<title>Dr. Lumora – Home</title>
<link rel="stylesheet" href="https://fonts.googleapis.com/css2?family=Open+Sans:wght@400;600&family=Hind:wght@400;500&family=Arimo:wght@400&display=swap">
<style>
:root{
  --brand:#008bcd;
  --brand-dark:#0a78b8;
  --brand-soft:#8fc6e6;
  --ink:#333;
  --muted:#9a9a9a;
  --line:#d4d4d4;
  --panel:#f1f2f3;
  --topbar:#3a3a3a;
  --white:#fff;
}
*{margin:0;padding:0;box-sizing:border-box}
html,body{width:751px;height:1200px;overflow:hidden;background:var(--white)}
body{position:relative;font-family:"Hind",sans-serif;color:var(--ink)}
.abs{position:absolute}

/* top language bar */
.lang-bar{left:0;top:0;width:751px;height:13px;background:var(--topbar)}
.lang{top:2px;font:400 5.5px/9px "Arimo",sans-serif;color:#ddd;display:flex;align-items:center;gap:3px}
.lang i{display:inline-block;width:8px;height:8px;border-radius:50%;background:#c9d4e6}
.lang.zh i{background:#e4e4e4}
.lang-sep{left:661px;top:2px;width:1px;height:9px;background:#888}

/* hero */
.hero{left:0;top:13px;width:751px;height:461px;
  background:linear-gradient(180deg,#c9d3d6 0%,#aeb9b4 30%,#8f8a80 60%,#6d5e58 100%)}
.brand{left:46px;top:36px;display:flex;align-items:center;gap:8px}
.brand-dot{width:34px;height:34px;border-radius:50%;background:var(--brand)}
.brand-name{font:600 25px/1 "Open Sans",sans-serif;color:var(--brand)}
.search{left:456px;top:38px;width:168px;height:21px;border-radius:11px;background:rgba(255,255,255,.92);
  border:1px solid #ddd;font:400 8px/19px "Hind",sans-serif;color:#bbb;padding-left:10px}
.search svg{position:absolute;right:8px;top:4px}
.login{left:648px;top:40px;width:55px;height:18px;background:#555;color:#fff;
  font:500 8.5px/18px "Hind",sans-serif;text-align:center;letter-spacing:.3px}

/* navigation */
.nav{left:0;top:474px;width:751px;height:44px;background:var(--white);border-bottom:2px solid var(--brand)}
.nav a{position:absolute;top:0;height:42px;font:400 11.5px/44px "Hind",sans-serif;color:var(--brand);text-decoration:none;transform:translateX(-50%)}
.nav a.active{left:134.5px;width:55px;text-align:center;background:var(--brand);color:#fff;height:44px}

/* membership */
.member{left:0;top:518px;width:751px;height:300px;
  background:linear-gradient(120deg,#8ec2e2 0%,#b9daee 35%,#7fb6dc 65%,#a9d2ec 100%)}
.member-title{left:48px;top:558px;font:400 20.5px/1 "Open Sans",sans-serif;color:#fff}
.perks{left:76px;top:603px;list-style:none}
.perks li{height:37.6px;display:flex;align-items:center;gap:13px;font:400 13.5px/1 "Hind",sans-serif;color:#fff}
.signup{left:374px;top:534px;width:348px;height:271px;border-radius:9px;background:rgba(225,240,250,.75)}
.field{height:26px;border:1px solid var(--brand-soft);background:#fff;font:400 10.5px/24px "Hind",sans-serif;color:var(--brand-soft);padding-left:9px}
.dob-label{left:387px;top:720px;font:500 12px/1 "Hind",sans-serif;color:var(--brand)}
.select{height:26px;border:1px solid var(--brand-soft);background:#fff;font:400 10.5px/24px "Hind",sans-serif;color:var(--brand-soft);text-align:center;padding-right:24px}
.select b{position:absolute;right:0;top:3px;width:23px;height:18px;border-left:1px solid var(--brand-soft)}
.select b::after{content:"";position:absolute;left:7px;top:6px;border:4px solid transparent;border-top:6px solid var(--brand)}
.btn-signup{left:512px;top:766px;width:64px;height:23px;background:var(--brand);color:#fff;border-radius:2px;
  font:500 10px/23px "Hind",sans-serif;text-align:center}

/* finder */
.finder{left:0;top:818px;width:751px;height:101px;background:var(--panel)}
.finder-tab{left:0;top:818px}
.finder-title{left:53px;top:858px;font:400 21px/1 "Open Sans",sans-serif;color:#fff}
.lbl{font:400 8px/1 "Arimo",sans-serif;color:#444}
.inp{height:15px;border:1px solid #ccc;border-radius:2px;background:#fff}
.dd{height:12px;border:1px solid #ccc;background:#fff;font:400 5.5px/10px "Arimo",sans-serif;color:#aaa;padding-left:5px}
.dd::after{content:"";position:absolute;right:3px;top:4px;border:2.5px solid transparent;border-top:3.5px solid #444}
.dd::before{content:"";position:absolute;right:10px;top:0;width:1px;height:10px;background:#ccc}
.radio{width:8px;height:8px;border:1px solid #999;border-radius:50%;background:#fff}
.radio.on::after{content:"";position:absolute;left:1.5px;top:1.5px;width:3px;height:3px;border-radius:50%;background:#333}
.btn{height:17px;font:400 8px/15px "Arimo",sans-serif;text-align:center}
.btn-reset{left:578px;top:890px;width:52px;border:1px solid var(--brand);color:var(--brand);background:#fff}
.btn-search{left:650px;top:890px;width:53px;background:var(--brand);color:#fff;border:1px solid var(--brand)}

/* results */
.results{left:25px;top:937px;width:700px;height:236px;border:1px solid #d6d6d6;border-radius:10px;background:#fff}
.empty{left:312px;top:1046px;display:flex;align-items:center;gap:6px;font:400 10px/1 "Hind",sans-serif;color:var(--brand)}
.footer{left:0;top:1183px;width:751px;text-align:center;font:400 5.5px/1 "Arimo",sans-serif;color:#888}
</style>
</head>
<body>

<div class="abs lang-bar"></div>
<div class="abs lang en" style="left:621px"><i></i>ENGLISH</div>
<div class="abs lang-sep"></div>
<div class="abs lang zh" style="left:666px"><i></i>CHINESE</div>

<div class="abs hero" role="img" aria-label="Lively photo of a group of young friends smiling and taking a selfie on a city street"></div>
<div class="abs brand"><span class="brand-dot"></span><span class="brand-name">Dr. Lumora</span></div>
<div class="abs search">Search . . .
  <svg width="11" height="11" viewBox="0 0 11 11"><circle cx="4.5" cy="4.5" r="3.5" fill="none" stroke="#8fc6e6" stroke-width="1.2"/><path d="M7 7l3 3" stroke="#8fc6e6" stroke-width="1.2"/></svg>
</div>
<div class="abs login">LOG IN</div>

<nav class="abs nav">
  <a class="active" href="#">Home</a>
  <a href="#" style="left:219px">Doctor List</a>
  <a href="#" style="left:336px">Health Information</a>
  <a href="#" style="left:438px">News</a>
  <a href="#" style="left:518px">About Us</a>
  <a href="#" style="left:612px">Contact Us</a>
</nav>

<section class="abs member" role="img" aria-label="Soft blue geometric background"></section>
<h2 class="abs member-title">Become a Dr. Lumora Member</h2>
<ul class="abs perks">
  <li><svg width="14" height="14" viewBox="0 0 14 14"><path d="M1 8l4 4L13 1" fill="none" stroke="#fff" stroke-width="2"/></svg>First- hand health news</li>
  <li><svg width="14" height="14" viewBox="0 0 14 14"><path d="M1 8l4 4L13 1" fill="none" stroke="#fff" stroke-width="2"/></svg>Exclusive promotions</li>
  <li><svg width="14" height="14" viewBox="0 0 14 14"><path d="M1 8l4 4L13 1" fill="none" stroke="#fff" stroke-width="2"/></svg>Instant health advices</li>
  <li><svg width="14" height="14" viewBox="0 0 14 14"><path d="M1 8l4 4L13 1" fill="none" stroke="#fff" stroke-width="2"/></svg>Free health seminars or talk</li>
  <li><svg width="14" height="14" viewBox="0 0 14 14"><path d="M1 8l4 4L13 1" fill="none" stroke="#fff" stroke-width="2"/></svg>Priority doctor appointments</li>
</ul>

<div class="abs signup"></div>
<div class="abs field" style="left:386px;top:554px;width:153px">First Name</div>
<div class="abs field" style="left:555px;top:554px;width:154px">Last Name</div>
<div class="abs field" style="left:386px;top:593px;width:323px">Email address</div>
<div class="abs field" style="left:386px;top:634px;width:323px">New password</div>
<div class="abs field" style="left:386px;top:674px;width:323px">Re-enter password</div>
<div class="abs dob-label">Date of Birth</div>
<div class="abs select" style="left:467px;top:716px;width:85px">Month<b></b></div>
<div class="abs select" style="left:557px;top:716px;width:62px">Day<b></b></div>
<div class="abs select" style="left:624px;top:716px;width:85px">Year<b></b></div>
<div class="abs btn-signup">SIGN UP</div>

<section class="abs finder"></section>
<svg class="abs finder-tab" width="230" height="101" viewBox="0 0 230 101"><path d="M0 0H176L230 101H0Z" fill="#008bcd"/></svg>
<svg class="abs" style="left:21px;top:858px" width="17" height="24" viewBox="0 0 17 24"><circle cx="8.5" cy="8.5" r="7.5" fill="none" stroke="#fff" stroke-width="1.4"/><circle cx="8.5" cy="6.5" r="2.5" fill="#fff"/><path d="M4 13c1-3 8-3 9 0" fill="#fff"/><path d="M2 19h13" stroke="#fff" stroke-width="1.4"/></svg>
<div class="abs finder-title">Find a Doctor</div>

<div class="abs lbl" style="left:223px;top:838px">Doctor's Name:</div>
<div class="abs inp" style="left:286px;top:834px;width:232px"></div>
<div class="abs lbl" style="left:554px;top:838px">Symptoms:</div>
<div class="abs dd" style="left:606px;top:836px;width:106px">Select a symptom</div>

<div class="abs lbl" style="left:247px;top:869px">Gender:</div>
<div class="abs radio on" style="left:287px;top:869px"></div>
<div class="abs lbl" style="left:300px;top:870px;font-size:6.5px">Male</div>
<div class="abs radio" style="left:287px;top:887px"></div>
<div class="abs lbl" style="left:300px;top:888px;font-size:6.5px">Female</div>

<div class="abs lbl" style="left:362px;top:866px">Phone Number:</div>
<div class="abs inp" style="left:427px;top:864px;width:91px;height:12px"></div>
<div class="abs lbl" style="left:554px;top:866px">District:</div>
<div class="abs dd" style="left:606px;top:864px;width:106px">Select a district</div>

<div class="abs lbl" style="left:362px;top:892px">Specialism:</div>
<div class="abs dd" style="left:427px;top:890px;width:91px">Select a specialism</div>
<div class="abs btn btn-reset">RESET</div>
<div class="abs btn btn-search">SEARCH</div>

<section class="abs results"></section>
<div class="abs empty">
  <svg width="12" height="12" viewBox="0 0 12 12"><circle cx="5" cy="5" r="4" fill="none" stroke="#008bcd" stroke-width="1.2"/><path d="M8 8l3.5 3.5" stroke="#008bcd" stroke-width="1.2"/></svg>
  No Results Found
</div>

<footer class="abs footer">© Dr. Lumora. All Rights Reserved.</footer>

</body>
</html>
```